Business Card Design Project

Company Name is Harbor Bail Bonds
Name: Marlene Hodgkin
Address is 412 Orchard St. Bellingham, WA 98317
Phone # 360-518-2964
Agency Lic # 4861
Agent Lic # 7142

I would like a business card with a rustic fence background and a 4 leaf clover. Also a pink line that will include my name and address. Different clover then shown.

On the back side I would like Next Court Date that include Date, Time and Location

I have attached my idea but this is blurry and business name and phone number seemed to be faded out along with Agent #s. This is the idea I like but don't like this design.

```html
<!DOCTYPE html>
<html lang="en">
<head>
<meta charset="utf-8">
<title>Harbor Bail Bonds – Business Card</title>
<link rel="stylesheet" href="https://fonts.googleapis.com/css2?family=Alfa+Slab+One&family=Fresca&family=Open+Sans:wght@400;600&display=swap">
<style>
  :root {
    --backdrop: #a3a3a3;
    --wood-dark: #4a3121;
    --wood-mid: #6b4a33;
    --wood-light-1: #f1f1f1;
    --wood-light-2: #e4e4e4;
    --pink: #e063bf;
    --pink-band: rgba(234, 98, 200, 0.94);
    --clover: #6db64e;
    --white: #ffffff;
  }
  * { box-sizing: border-box; margin: 0; padding: 0; }
  html, body { width: 1200px; height: 1200px; overflow: hidden; }
  body { background: var(--backdrop); position: relative; font-family: "Open Sans", sans-serif; }

  .card {
    position: absolute;
    left: 245px;
    width: 711px;
    height: 426px;
    overflow: hidden;
    box-shadow: 0 3px 8px rgba(0,0,0,0.25);
  }
  .card--front { top: 157px; }
  .card--back { top: 618px; }

  .wood-dark {
    position: absolute; inset: 0;
    background: linear-gradient(90deg, var(--wood-dark), var(--wood-mid) 30%, var(--wood-dark) 55%, var(--wood-mid) 80%, var(--wood-dark));
  }
  .wood-light {
    position: absolute; inset: 0;
    background: linear-gradient(90deg, var(--wood-light-1), var(--wood-light-2) 35%, var(--wood-light-1) 60%, var(--wood-light-2) 85%, var(--wood-light-1));
  }

  .company-name {
    position: absolute; left: 73px; top: 58px;
    font-family: "Alfa Slab One", serif; font-weight: 400;
    font-size: 37px; line-height: 50px; color: #f2f2f2;
    text-shadow: 2px 2px 3px rgba(0,0,0,0.6);
    white-space: nowrap;
  }

  .name-band {
    position: absolute; left: 0; right: 0; top: 137px; height: 193px;
    background: var(--pink-band);
  }
  .clover-art {
    position: absolute; left: 453px; top: 0; width: 258px; height: 292px;
    border-radius: 46% 0 0 50% / 50% 0 0 50%;
    background: radial-gradient(ellipse at 55% 50%, #74bd55 0%, var(--clover) 70%);
  }

  .agent-name {
    position: absolute; left: 75px; top: 175px;
    font-family: "Fresca", sans-serif; font-size: 38px; line-height: 44px;
    color: var(--white); white-space: nowrap;
  }
  .contact-line {
    position: absolute; left: 75px; height: 28px;
    display: flex; align-items: center; gap: 21px;
    font-family: "Fresca", sans-serif; font-size: 22px; line-height: 28px;
    color: var(--white); white-space: nowrap;
  }
  .contact-line--address { top: 229px; }
  .contact-line--phone { top: 260px; }
  .contact-line svg { width: 24px; height: 22px; flex: none; }

  .licenses {
    position: absolute; left: 549px; top: 344px;
    font-size: 16px; line-height: 23px; color: #f3f3f3;
  }

  .court-title {
    position: absolute; left: 0; right: 0; top: 87px;
    text-align: center; font-weight: 600; font-size: 30px; line-height: 40px; color: var(--pink);
  }
  .field {
    position: absolute; display: flex; align-items: flex-end;
    font-size: 21px; line-height: 28px; color: var(--pink); white-space: nowrap;
  }
  .field__line { border-bottom: 2px solid var(--pink); width: 204px; margin-left: 10px; margin-bottom: 4px; }
  .field--time .field__line { margin-left: 18px; }
  .field--location .field__line { margin-left: 15px; }
  .field--date { left: 76px; top: 172px; }
  .field--time { left: 359px; top: 172px; }
  .field--location { left: 199px; top: 214px; }

  .web-band {
    position: absolute; left: 0; right: 0; top: 316px; height: 44px;
    background: var(--pink);
    display: flex; align-items: center; justify-content: center;
    font-size: 21px; color: var(--white);
  }
</style>
</head>
<body>
  <section class="card card--front">
    <div class="wood-dark" role="img" aria-label="Rustic dark wooden fence boards"></div>
    <h1 class="company-name">Harbor Bail Bonds</h1>
    <div class="name-band"></div>
    <div class="clover-art" role="img" aria-label="Green four leaf clover illustration"></div>
    <p class="agent-name">Marlene Hodgkin</p>
    <p class="contact-line contact-line--address">
      <svg viewBox="0 0 24 24" fill="none" stroke="#fff" stroke-width="1.5"><path d="M5 3l4 4-2 3c1 2.5 3.5 5 6 6l3-2 4 4-3 3C10 20 4 14 2 6z"/><path d="M14 3a7 7 0 0 1 7 7M14 7a3 3 0 0 1 3 3"/></svg>
      <span>412 Orchard St. Bellingham, WA 98317</span>
    </p>
    <p class="contact-line contact-line--phone">
      <svg viewBox="0 0 24 22" fill="none" stroke="#fff" stroke-width="1.5"><rect x="1" y="3" width="22" height="16"/><path d="M1 3l11 9 11-9M1 19l8-7M23 19l-8-7"/></svg>
      <span>360-518-2964</span>
    </p>
    <p class="licenses">Agency Lic # 4861<br>Agent Lic # 7142</p>
  </section>

  <section class="card card--back">
    <div class="wood-light" role="img" aria-label="Whitewashed wooden fence boards"></div>
    <h2 class="court-title">Next Court Date.</h2>
    <div class="field field--date">Date :<span class="field__line"></span></div>
    <div class="field field--time">Time:<span class="field__line"></span></div>
    <div class="field field--location">Location :<span class="field__line"></span></div>
    <div class="web-band">www.harborbailbondsnw.com</div>
  </section>
</body>
</html>
```